Disability Service Provider Expo Banner that will stand out amongst the competition

We would like to have a two banners designed to be able to display at expos that outline the services that we provide as a company. We are a disability service provider who aims to provider services to increase the independence of those living with a disability. We would like the banners to follow consistent themes/designs from other marketing material that we have (see brief for designs). One of the banners will be for the allied health services we provide (exercise physiology and occupational therapy) and the other banner will be promoting the our support worker, programs, and short-term accommodation. Our main colour schemes for therapy are black, yellow, and white. For our other services we utilise yellow, blue, and magenta as part of our colour pallet. Please utilise the information from the flyers, colours, and logos all located in the design brief. The style of banner can be seen in the images upload in the brief.

Target Market(s)

Parents and carers of those who livce with a disability, and seeking their business over our competitors

Industry/Entity Type

Disability Service and Health Provider

Colors

Designer to choose colors to be used in the design.

Requirements
Must have
• Eye catching, limited text
Nice to have
• Split services across a few banners
Should not have
• Lots of words

```html
<!DOCTYPE html>
<html lang="en">
<head>
<meta charset="utf-8">
<title>Brightvale Pull Up Banners</title>
<link href="https://fonts.googleapis.com/css2?family=Gochi+Hand&family=Montserrat:ital,wght@0,400;0,600;0,700;0,800;1,800&display=swap" rel="stylesheet">
<style>
  :root {
    --black: #000000;
    --yellow: #f2da36;
    --white: #ffffff;
    --stage: #cdcdcd;
    --pill-grey: #cfd0d2;
    --ink: #111111;
  }
  * { box-sizing: border-box; margin: 0; padding: 0; }
  html, body { width: 1187px; height: 1200px; overflow: hidden; }
  body {
    background: var(--stage);
    font-family: "Montserrat", Arial, sans-serif;
    position: relative;
  }
  .banner {
    position: absolute;
    top: 116px;
    width: 410px;
    height: 932px;
    background: var(--black);
    overflow: hidden;
  }
  .banner--therapy { left: 164px;
    background: linear-gradient(180deg, #000 0%, #000 42%, #1a1a1a 50%, #3a3d40 75%, #1b1b1b 90%, #000 100%);
  }
  .banner--services { left: 616px; }

  .brand { position: absolute; top: 40px; left: 0; right: 0; text-align: center; }
  .brand__dot {
    display: block; width: 34px; height: 34px; border-radius: 50%;
    background: var(--yellow); margin: 0 auto 22px;
  }
  .brand__name {
    font-weight: 800; font-size: 46px; letter-spacing: 1px;
    color: var(--white); line-height: 1;
  }

  .headline {
    position: absolute; top: 190px; left: 0; right: 0; text-align: center;
    font-family: "Gochi Hand", cursive; color: var(--yellow);
    font-size: 60px; line-height: 54px; text-transform: uppercase;
  }
  .intro {
    position: absolute; top: 322px; left: 20px; right: 20px; text-align: center;
    color: var(--white); font-size: 17.5px; line-height: 22.5px;
  }
  .intro strong { font-weight: 700; }

  .hero-photo {
    position: absolute; top: 399px; left: 0; width: 410px; height: 318px;
    background: linear-gradient(180deg, rgba(0,0,0,0) 0%, #8fb3c8 18%, #6b8fa6 45%, #4a5157 75%, rgba(40,40,40,0.6) 100%);
  }

  .tags { position: absolute; top: 719px; left: 0; width: 410px; height: 32px; }
  .tag {
    position: absolute; top: 0; height: 32px; border-radius: 5px;
    font-weight: 800; font-style: italic; font-size: 15px; color: var(--ink);
    display: flex; align-items: center; justify-content: center;
    box-shadow: 0 6px 8px rgba(0,0,0,0.45);
  }
  .tag--grey { background: var(--pill-grey); }
  .tag--yellow { background: var(--yellow); }

  .contact-cloud { position: absolute; left: 0; top: 795px; width: 410px; height: 137px; }
  .contact {
    position: absolute; left: 0; right: 0; top: 848px; text-align: center; color: var(--ink);
  }
  .contact__phone { font-size: 25px; line-height: 30px; display: flex; align-items: center; justify-content: center; gap: 6px; }
  .contact__phone strong, .contact__web strong { font-weight: 700; }
  .contact__web { font-size: 22.5px; line-height: 30px; }

  .section-title {
    position: absolute; top: 190px; left: 36px; right: 36px; height: 27px;
  }
  .section-title::before {
    content: ""; position: absolute; left: 0; right: 0; top: 13px; height: 1px;
    background: linear-gradient(90deg, rgba(242,218,54,0), var(--yellow) 40%, var(--yellow) 60%, rgba(242,218,54,0));
  }
  .section-title span {
    position: absolute; left: 98px; width: 146px; height: 27px; border-radius: 14px;
    background: var(--yellow); color: var(--ink); font-weight: 800; font-size: 17.5px;
    display: flex; align-items: center; justify-content: center;
  }

  .service {
    position: absolute; width: 160px; height: 143px; border: 2px solid var(--yellow);
    border-radius: 8px; background: var(--yellow); overflow: hidden;
  }
  .service__photo { height: 106px; border-radius: 6px 6px 0 0; }
  .service__label {
    height: 33px; display: flex; align-items: center; justify-content: center; text-align: center;
    font-weight: 700; font-size: 12.5px; line-height: 14.5px; color: var(--ink);
  }
  .col-1 { left: 37px; } .col-2 { left: 208px; }
  .row-1 { top: 243px; } .row-2 { top: 396px; } .row-3 { top: 548px; }

  .values {
    position: absolute; top: 713px; left: 26px; right: 26px; height: 50px;
    display: flex; align-items: center; justify-content: space-between;
    font-family: "Gochi Hand", cursive; color: var(--white); font-size: 23px; line-height: 23px;
    text-transform: uppercase; text-align: center;
  }
  .values__dot { width: 18px; height: 18px; border-radius: 50%; background: var(--yellow); }
</style>
</head>
<body>

<section class="banner banner--therapy">
  <div class="brand"><span class="brand__dot"></span><div class="brand__name">BRIGHTVALE</div></div>
  <h1 class="headline">Exercise<br>Physiology</h1>
  <p class="intro">Improve your <strong>health, quality of life, &amp; independence</strong> with the help of our Excersise Physiologist!</p>
  <div class="hero-photo" role="img" aria-label="Photo of a woman with a prosthetic leg doing sit-ups on a gym mat, guided by an exercise physiologist"></div>
  <div class="tags">
    <div class="tag tag--grey" style="left:27px;width:107px;">GET FIT</div>
    <div class="tag tag--yellow" style="left:141px;width:132px;">BE HEALTHY</div>
    <div class="tag tag--grey" style="left:279px;width:107px;">HAVE FUN</div>
  </div>
  <svg class="contact-cloud" viewBox="0 0 410 137" aria-hidden="true">
    <path fill="#f2da36" d="M0,50 L28,64 C24,8 170,-18 186,36 C205,22 245,22 262,36 C290,-8 385,8 382,72 C395,68 404,64 410,60 L410,137 L0,137 Z"/>
  </svg>
  <div class="contact">
    <div class="contact__phone">
      <svg width="24" height="24" viewBox="0 0 24 24" aria-hidden="true"><circle cx="12" cy="12" r="12" fill="#111"/><path fill="#f2da36" d="M8.2 6.2l1.8-.3 1.2 2.8-1.3 1c.6 1.4 1.6 2.5 3 3.2l1-1.3 2.8 1.2-.3 1.8c-.2.7-.9 1.1-1.6 1-4-.6-7.1-3.7-7.6-7.7-.1-.7.3-1.4 1-1.6z"/></svg>
      <span>Call <strong>1800 000 123</strong></span>
    </div>
    <div class="contact__web">www.<strong>brightvale.com</strong>.au</div>
  </div>
</section>

<section class="banner banner--services">
  <div class="brand"><span class="brand__dot"></span><div class="brand__name">BRIGHTVALE</div></div>
  <h2 class="section-title"><span>Our Services</span></h2>

  <div class="service col-1 row-1"><div class="service__photo" role="img" aria-label="Photo of a support worker and a young woman smiling outdoors" style="background:linear-gradient(160deg,#e9eef0,#b79a86 55%,#5f6e3e)"></div><div class="service__label">Support Workers</div></div>
  <div class="service col-2 row-1"><div class="service__photo" role="img" aria-label="Photo of three men in wheelchairs together outdoors" style="background:linear-gradient(160deg,#a9b59a,#6e6a62 55%,#2d3442)"></div><div class="service__label">Day Programs<br>&amp; Workshops</div></div>
  <div class="service col-1 row-2"><div class="service__photo" role="img" aria-label="Photo of a group in blue shirts joining hands in a huddle" style="background:linear-gradient(160deg,#5c7a4a,#8fb0cf 55%,#6e8fb3)"></div><div class="service__label">Group Activities</div></div>
  <div class="service col-2 row-2"><div class="service__photo" role="img" aria-label="Photo of two women baking together in a kitchen" style="background:linear-gradient(160deg,#d8d8d4,#b9a58a 55%,#8a8c90)"></div><div class="service__label">Living Skills<br>Programs</div></div>
  <div class="service col-1 row-3"><div class="service__photo" role="img" aria-label="Photo of friends taking a cheerful group selfie on holiday" style="background:linear-gradient(160deg,#9aa6b4,#c9a07f 50%,#8b5a4a)"></div><div class="service__label">STA/ Supported<br>Holiday</div></div>
  <div class="service col-2 row-3"><div class="service__photo" role="img" aria-label="Photo of a therapist and a young woman doing a hands-on activity at a table" style="background:linear-gradient(160deg,#d4d8dc,#c7c4c0 55%,#e8e4e0)"></div><div class="service__label">Therapies</div></div>

  <div class="values">
    <span>More<br>Independence.</span>
    <span class="values__dot"></span>
    <span>More<br>Choice.</span>
    <span class="values__dot"></span>
    <span>More<br>Fun.</span>
  </div>

  <svg class="contact-cloud" viewBox="0 0 410 137" aria-hidden="true">
    <path fill="#f2da36" d="M0,50 L28,64 C24,8 170,-18 186,36 C205,22 245,22 262,36 C290,-8 385,8 382,72 C395,68 404,64 410,60 L410,137 L0,137 Z"/>
  </svg>
  <div class="contact">
    <div class="contact__phone">
      <svg width="24" height="24" viewBox="0 0 24 24" aria-hidden="true"><circle cx="12" cy="12" r="12" fill="#111"/><path fill="#f2da36" d="M8.2 6.2l1.8-.3 1.2 2.8-1.3 1c.6 1.4 1.6 2.5 3 3.2l1-1.3 2.8 1.2-.3 1.8c-.2.7-.9 1.1-1.6 1-4-.6-7.1-3.7-7.6-7.7-.1-.7.3-1.4 1-1.6z"/></svg>
      <span>Call <strong>1800 000 123</strong></span>
    </div>
    <div class="contact__web">www.<strong>brightvale.com</strong>.au</div>
  </div>
</section>

</body>
</html>
```